Complete web design based around only our company logo

I need someone to build a web page based around our company logo. I will provide other sites that we like and would want our site to be similar to.
Updates

Please look at these websites to get an idea of our industry

larkspur minerals
tov minerals
granite royalty
windmere energy
harlow energy

Our company buys mineral rights, and royalties from mineral owners all over the united states.  We also lease minerals as well. 

What we are trying to have designed is a fully functioning website that you upload to our webhost after we approve of final design.  

Target Market(s)

Oil and Gas/Mineral Owners

Industry/Entity Type

It Company

Font styles to use
Serif
Sans Serif

Colors
9ccb3b

Requirements
Must have
• Quick Contact form

```html
<!DOCTYPE html>
<html lang="en">
<head>
<meta charset="utf-8">
<title>Tamberlin Holdings</title>
<link href="https://fonts.googleapis.com/css2?family=Open+Sans:wght@300;400;600;700&display=swap" rel="stylesheet">
<style>
:root{
  --green:#9ccb3b;
  --green-dark:#4e8d12;
  --green-mid:#86b820;
  --green-head:#7cb82f;
  --nav-top:#a2d24a;
  --nav-bottom:#82bc2c;
  --nav-active:#5e9e1c;
  --field-text:#d3eb95;
  --text:#222;
  --muted:#777;
  --band:#f5f5f5;
  --footer:#f1f1f1;
  --social-a:#3b5b9a;
  --social-b:#39c2d7;
}
*{margin:0;padding:0;box-sizing:border-box}
html,body{width:1200px;height:1097px;overflow:hidden}
body{font-family:"Open Sans",Arial,sans-serif;background:#fff;color:var(--text);position:relative}
.abs{position:absolute}
.top-band{left:0;top:0;width:1200px;height:266px;background:var(--band)}
.brand{left:123px;top:104px;font-weight:600;font-size:20px;line-height:26px;color:var(--text)}
.search{left:847px;top:39px;width:234px;height:33px;background:#fff;border:1px solid #eee;font-size:13px;color:#bbb;padding:9px 10px;font-weight:300}
.search svg{position:absolute;right:8px;top:6px}
.phone{right:119px;top:100px;font-size:30px;line-height:38px;font-weight:300;color:var(--text)}
.main-nav{left:120px;top:141px;width:960px;height:63px;background:linear-gradient(var(--nav-top),var(--nav-bottom));display:flex}
.main-nav a{color:#fff;text-decoration:none;font-weight:700;font-size:14px;line-height:63px;padding:3px 19px 0;border-right:1px solid rgba(255,255,255,.25)}
.main-nav a.active{background:var(--nav-active);padding:3px 21px 0 32px}
.main-nav a:last-child{border-right:none}
.hero{left:119px;top:213px;width:961px;height:360px;background:linear-gradient(100deg,#5c6064 0%,#9a9ea2 30%,#c8cbcd 50%,#6a6f78 70%,#3b4154 100%)}
.caption{left:152px;top:331px;width:361px;height:173px;background:rgba(255,255,255,.85);padding:14px 10px 14px 15px}
.caption h1{font-size:28px;font-weight:400;line-height:38px;margin-bottom:0}
.caption h1 b{color:var(--green-dark);font-weight:600}
.caption p{font-size:14px;line-height:26px;font-weight:300;color:#333;letter-spacing:-.25px}
.dots{left:161px;top:538px;display:flex;gap:4px}
.dots span{width:16px;height:16px;border-radius:50%;background:#fff}
.dots span.on{background:var(--green)}
.quick{left:765px;top:224px;width:297px;height:339px;background:var(--green);padding:20px 21px}
.quick h2{color:#fff;font-size:19px;font-weight:600;line-height:26px;margin:0 0 18px 2px}
.field{height:44px;background:var(--green-mid);border:1px solid #76a51c;margin-bottom:9px;font-size:13px;color:var(--field-text);padding:13px 10px;font-weight:400}
.submit{left:855px;top:504px;width:110px;height:36px;background:linear-gradient(#fff,#e4e4e4);border:1px solid #ccc;font-weight:700;font-size:13px;text-align:center;line-height:34px;color:var(--text)}
.section-title{color:var(--green-head);font-size:19px;font-weight:600;line-height:26px}
.welcome{left:120px;top:617px;width:632px}
.welcome p{font-size:14px;line-height:26px;font-weight:300;color:var(--muted);margin-top:13px;letter-spacing:-.1px}
.welcome p+p{margin-top:26px}
.news{left:773px;top:617px;width:300px}
.news-arrows{position:absolute;right:2px;top:6px}
.news-item{position:absolute;left:-2px;width:302px}
.news-photo{width:119px;height:88px}
.news-date{position:absolute;left:11px;top:96px;font-weight:700;font-size:14px}
.news-text{position:absolute;left:129px;top:-8px;width:175px;font-size:14px;line-height:26px;font-weight:300;color:var(--muted)}
.footer{left:0;top:1003px;width:1200px;height:94px;background:var(--footer)}
.foot-links{left:128px;top:1022px;font-size:13.5px;color:#333}
.foot-links span{margin:0 19px}
.copy{left:128px;top:1060px;font-size:13.5px;color:#333}
.social{left:977px;top:1027px;display:flex;gap:4px}
.social span{width:45px;height:45px;border-radius:50%}
.social .s1{background:var(--social-a)}
.social .s2{background:var(--social-b)}
</style>
</head>
<body>
<div class="abs top-band"></div>

<header>
  <div class="abs brand">Tamberlin Holdings</div>
  <div class="abs search">Search
    <svg width="24" height="20" viewBox="0 0 24 20"><circle cx="8" cy="8" r="5.5" fill="none" stroke="#999" stroke-width="2"/><line x1="12" y1="12" x2="21" y2="17" stroke="#999" stroke-width="3" stroke-linecap="round"/></svg>
  </div>
  <div class="abs phone">1-800-555-0142</div>
  <nav class="abs main-nav">
    <a class="active" href="#">HOME</a><a href="#">ABOUT US</a><a href="#">SERVICES</a><a href="#">OIL &amp; MINERALS</a><a href="#">CAREERS</a><a href="#">CONTACT US</a>
  </nav>
</header>

<section>
  <div class="abs hero" role="img" aria-label="Refinery pipework with a worker in a hard hat and overalls"></div>
  <div class="abs caption">
    <h1>Tamberlin <b>Holdings</b></h1>
    <p>Lorem Ipsum is simply dummy text of the printing and typesetting industry. Lorem Ipsum has been the industry's standard dummy text ever since the 1500s, when an unknown printer</p>
  </div>
  <div class="abs dots"><span class="on"></span><span></span><span></span><span></span></div>
  <form class="abs quick">
    <h2>Quick Contact</h2>
    <div class="field">Name</div>
    <div class="field">E-Mail</div>
    <div class="field">Phone</div>
    <div class="field">Company Name</div>
  </form>
  <div class="abs submit">SUBMIT</div>
</section>

<main>
  <div class="abs welcome">
    <h2 class="section-title">Welcome to Tamberlin Holdings</h2>
    <p>Lorem Ipsum is simply dummy text of the printing and typesetting industry. Lorem Ipsum has been the industry's standard dummy text ever since the 1500s, when an unknown printer took a galley of type and scrambled it to make a type specimen book. It has survived not only five centuries, but also the leap into electronic typesetting, remaining essentially unchanged. It was popularised in the 1960s with the release of transfer sheets containing Lorem Ipsum passages, and more recently with desktop publishing software like early layout tools including versions of Lorem Ipsum.</p>
    <p>Lorem Ipsum is simply dummy text of the printing and typesetting industry. Lorem Ipsum has been the industry's standard dummy text ever since the 1500s, when an unknown printer took a galley of type and scrambled it to make a type specimen book. It has survived not only five centuries, but also the leap into electronic typesetting, remaining essentially unchanged.</p>
  </div>

  <div class="abs news">
    <h2 class="section-title">Latest News</h2>
    <svg class="news-arrows" width="26" height="16" viewBox="0 0 26 16"><polyline points="9,2 3,8 9,14" fill="none" stroke="#666" stroke-width="2.5"/><polyline points="17,2 23,8 17,14" fill="none" stroke="#666" stroke-width="2.5"/></svg>
    <div class="news-item" style="top:50px">
      <div class="news-photo" role="img" aria-label="Oil pump jack at sunset" style="background:linear-gradient(#3d6fa8,#e2a35a 60%,#2b3550)"></div>
      <div class="news-date">March 6 ,2014</div>
      <div class="news-text">Lorem Ipsum is simply dummy text of the printing and typesetting industry. Lorem Ipsum has been the industry's standard</div>
    </div>
    <div class="news-item" style="top:203px">
      <div class="news-photo" role="img" aria-label="Offshore platform lit at night" style="background:linear-gradient(#1f4f8e,#0f2a55 55%,#c46b22 75%,#14223f)"></div>
      <div class="news-date">March 6 ,2014</div>
      <div class="news-text">Lorem Ipsum is simply dummy text of the printing and typesetting industry. Lorem Ipsum has been the industry's standard</div>
    </div>
  </div>
</main>

<footer>
  <div class="abs footer"></div>
  <div class="abs foot-links">Home<span>|</span>About Us<span>|</span>Services<span>|</span>Oil &amp; Minerals<span>|</span>Careers<span>|</span>Contact Us</div>
  <div class="abs copy">© 2014 Company&nbsp; Name , All Rights reserved</div>
  <div class="abs social"><span class="s1" aria-label="Social link"></span><span class="s2" aria-label="Social link"></span></div>
</footer>
</body>
</html>
```